Lantern Square, Steady Course. (Website Design)

We are launching a new bipartisan civic movement: Lantern Square. Steady Course.
The mission is this: Americans deserve a government that is legally required to serve them honestly.
We are looking for a world-class website designer capable of creating an emotionally powerful, modern, cinematic landing page experience that feels larger than politics.
This is not a campaign website for a political party or candidate. We are not looking for a red, white, and blue page with stripes, or American flags, or stock footage of smiling people in a voting booth. We are looking for an emotional and cinematic experience through and through.
The visual direction should feel:
Historic
Hopeful
American
Emotional
Cinematic
Trustworthy
Timeless
The goal is to make visitors feel that they are witnessing the beginning of something important and want to be part of it in the end.
Primary Objective:
Inspire visitors to participate in a one-minute survey and cast their vote.
The survey itself is extremely short and takes approximately one minute to complete.
Everything on the page should ultimately guide visitors toward this action while creating enough curiosity, trust, emotional engagement, and excitement that they feel compelled to take part in the movement.
Audience:
The audience is ordinary Americans across the political spectrum: Democrats, Republicans, Independents.
The design should feel unifying and welcoming.
It should avoid looking partisan, ideological, activist, or government-issued.
Creative Freedom:
We are intentionally giving designers substantial creative freedom.
We are not looking for someone to simply arrange content into predefined sections.
Instead, we are looking for a designer who can think strategically about user experience and persuasion.
The ideal design is as minimal as possible, but you may always:
Use as many sections as you believe are necessary.
Use as many images as you believe are necessary.
Include storytelling elements.
Include data visualizations.
Include timelines.
Include videos.
Include animations.
Include or exclude sections as you see fit.
Reorganize the flow entirely.
We uploaded some files containing text and section suggestions. You don’t have to use them.
We also uploaded some images to convey the general feel we’re looking for.
We are much more interested in the effectiveness of the overall experience than in any specific layout.
What success looks like:
Think outside the box.
Please do not create another generic political website. We have already explored those approaches.
We are looking for something different.
The winning design will be the one that most effectively guides visitors from curiosity to belief to participation.
When a visitor reaches the end of the experience, they should feel:
This is bigger than politics.
This is something I can support regardless of party.
This feels credible.
This feels hopeful.
I want to be part of this.
Use the survey results, the research findings, the principles, the storytelling, or any other elements you believe will help build trust and inspire participation.
Don't just impress us with flashy visuals. Impress us with a website experience that inspires people to become part of the movement and cast their vote.
The final call-to-action should feel like the natural conclusion of the journey, not a request for engagement.
Our goal is not simply to inform visitors. Our goal is to inspire them to cast their vote.
Prioritize emotional impact, storytelling, clarity, and persuasion over decorative design elements.
Final words:
Design a website experience that successfully inspires visitors to take the survey and cast their vote.
Think like a storyteller, not just a designer.
Thank you for your interest in the project.
Best of luck.

```html
<!DOCTYPE html>
<html lang="en">
<head>
<meta charset="utf-8">
<title>Lantern Square. Steady Course.</title>
<link href="https://fonts.googleapis.com/css2?family=Playfair+Display:wght@400;500;600;700&family=Inter:wght@400;500;600;700&display=swap" rel="stylesheet">
<style>
:root{
  --hero:#70757c;
  --navy:#0b111c;
  --navy-card:#131b28;
  --gold:#d4ae62;
  --slate:#5d6370;
  --sand:#f1ece4;
  --paper:#f5f5f3;
  --cream:#f3f0ea;
  --ink:#1e2430;
  --muted:#4b505a;
  --charcoal:#141414;
  --card-dark:#272727;
  --white:#ffffff;
  --play:#2f8fe0;
}
*{box-sizing:border-box;margin:0;padding:0}
html,body{width:1200px;height:3609px;overflow:hidden}
body{font-family:"Inter",sans-serif;color:var(--ink);background:var(--paper)}
section,footer{position:relative;width:1200px}

/* hero */
.hero{height:750px;background:var(--hero);color:var(--white)}
.hero .eyebrow{position:absolute;left:301px;top:211px;font-size:10px;letter-spacing:3px;color:#dfe1e4}
.hero h1{position:absolute;left:301px;top:240px;font-family:"Playfair Display",serif;font-weight:700;font-size:62px;line-height:69px;width:520px}
.hero .lede{position:absolute;left:301px;top:462px;font-size:16px;line-height:20px;width:460px;color:#e7e8ea}
.btn-gold{position:absolute;left:301px;top:526px;width:145px;height:35px;background:var(--gold);color:#1b1b1b;font-size:11px;font-weight:700;display:flex;align-items:center;justify-content:center}
.btn-ghost{position:absolute;left:460px;top:526px;width:225px;height:35px;border:1px solid #c9ccd0;color:var(--white);font-size:11px;display:flex;align-items:center;justify-content:center}
.pill{position:absolute;left:1013px;top:694px;width:165px;height:35px;border-radius:18px;background:var(--gold);color:#1b1b1b;font-size:10px;font-weight:700;display:flex;align-items:center;justify-content:center;box-shadow:0 2px 8px rgba(0,0,0,.2)}

/* stats */
.stats{height:526px;background:var(--navy);color:var(--white)}
.stats h2{position:absolute;left:165px;top:58px;font-family:"Playfair Display",serif;font-weight:500;font-size:32px;line-height:42px}
.stat-row{position:absolute;left:165px;top:177px;display:flex;gap:22px}
.stat{width:275px;height:112px;background:var(--navy-card);text-align:center;padding-top:28px}
.stat b{display:block;font-family:"Playfair Display",serif;font-size:40px;line-height:40px;color:var(--gold);font-weight:600}
.stat span{font-size:11px;color:#e6e8ec}
.timeline-label{position:absolute;left:165px;top:324px;font-size:11px;font-style:italic;color:#e0e2e6}
.bars{position:absolute;left:165px;top:362px;display:flex;gap:11px}
.bar{position:relative;width:209px;height:84px;background:var(--slate)}
.bar span{position:absolute;left:0;top:1px;font-size:11px;color:#eef0f3}
.bar i{position:absolute;left:0;bottom:0;width:100%;background:var(--gold)}

/* not left */
.forward{height:462px;background:var(--sand)}
.forward h2{position:absolute;left:165px;top:60px;font-family:"Playfair Display",serif;font-weight:500;font-size:28px;line-height:38px;color:var(--ink)}
.forward h2 em{font-style:normal;color:var(--gold)}
.photos{position:absolute;left:165px;top:206px;display:flex;gap:11px}
.photo{width:209px;height:200px}

/* goals */
.goals{height:330px;background:var(--paper)}
.goals h2{position:absolute;left:0;width:1200px;top:62px;text-align:center;font-family:"Playfair Display",serif;font-weight:500;font-size:28px}
.goal-row{position:absolute;left:165px;top:131px;display:flex;gap:22px}
.goal{width:275px;height:108px;background:var(--white);border-bottom:3px solid var(--gold);padding:24px 23px 0;box-shadow:0 1px 4px rgba(0,0,0,.05)}
.goal h3{font-family:"Playfair Display",serif;font-size:13px;font-weight:600;margin-bottom:2px}
.goal p{font-size:11.5px;line-height:14px;color:var(--muted)}

/* journey */
.journey{height:276px;background:var(--cream)}
.journey h2{position:absolute;left:165px;top:60px;font-family:"Playfair Display",serif;font-weight:500;font-size:24px}
.steps{position:absolute;left:165px;top:91px;display:flex;gap:23px}
.step{width:200px;height:119px;background:var(--white);text-align:center;padding-top:24px;box-shadow:0 1px 4px rgba(0,0,0,.06)}
.step svg{display:block;margin:0 auto 4px}
.step h3{font-family:"Playfair Display",serif;font-size:13px;font-weight:600}
.step p{font-size:11px;line-height:14px;color:var(--muted);width:150px;margin:0 auto}

/* agree */
.agree{height:345px;background:var(--paper)}
.agree h2{position:absolute;left:0;width:1200px;top:60px;text-align:center;font-family:"Playfair Display",serif;font-weight:500;font-size:17px}
.ring{position:absolute;top:124px;width:150px;text-align:center}
.ring svg{display:block;margin:0 auto}
.ring p{font-size:11px;line-height:14px;color:var(--muted);margin-top:14px}

/* voices */
.voices{height:405px;background:var(--charcoal);color:var(--white)}
.voices h2{position:absolute;left:165px;top:56px;font-family:"Playfair Display",serif;font-weight:500;font-size:26px}
.voice-row{position:absolute;left:165px;top:92px;display:flex;gap:23px}
.voice{width:200px;height:256px;background:var(--card-dark)}
.voice .shot{height:157px}
.voice .body{padding:14px 14px 0;font-size:11px;line-height:14px}
.voice b{display:block}
.voice .watch{display:block}
.voice .watch.small{font-size:8px;margin-top:1px}
.play{display:inline-block;width:8px;height:8px;background:var(--play);margin-right:3px;vertical-align:-1px}

/* final */
.final{height:436px;background:var(--paper)}
.final h2{position:absolute;left:0;width:1200px;top:56px;text-align:center;font-family:"Playfair Display",serif;font-weight:500;font-size:34px;line-height:41px}
.final .sub{position:absolute;left:0;width:1200px;top:152px;text-align:center;font-size:13px;color:var(--muted)}
.vote-card{position:absolute;left:350px;top:192px;width:500px;height:164px;background:var(--white);box-shadow:0 4px 20px rgba(0,0,0,.08);padding:24px 23px 0}
.vote-card h3{text-align:center;font-family:"Playfair Display",serif;font-weight:500;font-size:12px}
.vote-card p,.vote-card label{display:block;font-size:11px;line-height:14px;color:var(--ink)}
.vote-card label.no{margin-top:9px}
.radio{display:inline-block;width:9px;height:9px;border:1px solid #999;border-radius:50%;vertical-align:-1px;margin-right:4px}
.tick{display:inline-block;width:10px;height:10px;background:#4caf50;border-radius:2px;vertical-align:-1px;margin-right:3px}
.cross{color:#d9342b;font-weight:700;margin-right:3px}
.cast{position:absolute;left:23px;top:107px;width:454px;height:35px;background:var(--navy);color:var(--white);font-size:9px;font-weight:700;display:flex;align-items:center;justify-content:center}

footer{height:79px;background:var(--navy);text-align:center;color:#5c6370;font-size:11px;line-height:21px;padding-top:21px}
</style>
</head>
<body>

<section class="hero">
  <div class="eyebrow">THE NEXT CHAPTER OF AMERICA</div>
  <h1>The Next Chapter Begins With One Question.</h1>
  <p class="lede">What if government was legally required to serve the people honestly?</p>
  <div class="btn-gold">Cast Your Vote</div>
  <div class="btn-ghost">Watch 60-Second Introduction ↓</div>
  <div class="pill">✦ CAST YOUR VOTE ✦</div>
</section>

<section class="stats">
  <h2>Americans disagree on many things.<br>But almost everyone agrees on this.</h2>
  <div class="stat-row">
    <div class="stat"><b>18%</b><span>Trust in Government (2025)</span></div>
    <div class="stat"><b>76%</b><span>Public Frustration with Politics</span></div>
    <div class="stat"><b>81%</b><span>Believe System Is Divided</span></div>
  </div>
  <div class="timeline-label">Timeline: Public trust has eroded for decades</div>
  <div class="bars">
    <div class="bar"><span>1970</span><i style="height:59px"></i></div>
    <div class="bar"><span>1990</span><i style="height:38px"></i></div>
    <div class="bar"><span>2010</span><i style="height:22px"></i></div>
    <div class="bar"><span>2025</span><i style="height:11px"></i></div>
  </div>
</section>

<section class="forward">
  <h2>Not Left.<br>Not Right.<br><em>Forward.</em></h2>
  <div class="photos">
    <div class="photo" role="img" aria-label="People reviewing charts together at a table" style="background:linear-gradient(135deg,#b39a7e,#d9cfc3 60%,#8a7563)"></div>
    <div class="photo" role="img" aria-label="Worker installing solar panels under a clear sky" style="background:linear-gradient(160deg,#b9c4cf,#5f7186 60%,#3a4656)"></div>
    <div class="photo" role="img" aria-label="Laptop on a wooden desk with a cable and small device" style="background:linear-gradient(135deg,#c7b5a2,#8e8580 55%,#5c4d46)"></div>
    <div class="photo" role="img" aria-label="Volunteer carrying a box of food aid" style="background:linear-gradient(160deg,#4c4e55,#c9c4bb 55%,#8d6e4f)"></div>
  </div>
</section>

<section class="goals">
  <h2>What Is Lantern Square. Steady Course.</h2>
  <div class="goal-row">
    <div class="goal"><h3>Transparency</h3><p>Government cannot hide performance. Every action measurable, every record open.</p></div>
    <div class="goal"><h3>Accountability</h3><p>Promises become measurable obligations. Legal duty to serve honestly.</p></div>
    <div class="goal"><h3>Representation</h3><p>Citizens stay in control. A binding covenant between the people and public servants.</p></div>
  </div>
</section>

<section class="journey">
  <h2>The journey to restore trust</h2>
  <div class="steps">
    <div class="step">
      <svg width="12" height="20" viewBox="0 0 12 20"><circle cx="6" cy="5" r="4.5" fill="#e0383a"/><line x1="6" y1="9" x2="6" y2="19" stroke="#888" stroke-width="1.5"/></svg>
      <h3>Today</h3><p>Broken trust &amp; political deadlock</p></div>
    <div class="step">
      <svg width="14" height="20" viewBox="0 0 14 20"><path d="M7 2v15M2 12l5 5 5-5" fill="none" stroke="#d4ae62" stroke-width="1.5"/></svg>
      <h3>Reform</h3><p>Honest Governance Act drafted</p></div>
    <div class="step">
      <svg width="14" height="20" viewBox="0 0 14 20"><path d="M7 2v15M2 12l5 5 5-5" fill="none" stroke="#d4ae62" stroke-width="1.5"/></svg>
      <h3>Participation</h3><p>1 million voices demand change</p></div>
    <div class="step">
      <svg width="14" height="20" viewBox="0 0 14 20"><path d="M7 2v15M2 12l5 5 5-5" fill="none" stroke="#d4ae62" stroke-width="1.5"/></svg>
      <h3>Accountability</h3><p>Law binds all officials</p></div>
  </div>
</section>

<section class="agree">
  <h2>What Americans Already Agree On</h2>
  <div class="ring" style="left:361px">
    <svg width="86" height="86" viewBox="0 0 86 86"><circle cx="43" cy="43" r="40" fill="none" stroke="#e2e2e2" stroke-width="5"/><path d="M43 3A40 40 0 0 1 66.5 10.6" fill="none" stroke="#d4ae62" stroke-width="5"/><text x="43" y="48" text-anchor="middle" font-family="Inter,sans-serif" font-size="15" font-weight="600" fill="#1e2430">10%</text></svg>
    <p>84% want<br>accountability</p></div>
  <div class="ring" style="left:524px">
    <svg width="86" height="86" viewBox="0 0 86 86"><circle cx="43" cy="43" r="40" fill="none" stroke="#e2e2e2" stroke-width="5"/><path d="M43 3A40 40 0 0 1 66.5 10.6" fill="none" stroke="#d4ae62" stroke-width="5"/><text x="43" y="48" text-anchor="middle" font-family="Inter,sans-serif" font-size="15" font-weight="600" fill="#1e2430">10%</text></svg>
    <p>79% want transparency</p></div>
  <div class="ring" style="left:687px">
    <svg width="86" height="86" viewBox="0 0 86 86"><circle cx="43" cy="43" r="40" fill="none" stroke="#e2e2e2" stroke-width="5"/><path d="M43 3A40 40 0 0 1 66.5 10.6" fill="none" stroke="#d4ae62" stroke-width="5"/><text x="43" y="48" text-anchor="middle" font-family="Inter,sans-serif" font-size="15" font-weight="600" fill="#1e2430">10%</text></svg>
    <p>82% want measurable<br>outcomes</p></div>
</section>

<section class="voices">
  <h2>Voices Across America</h2>
  <div class="voice-row">
    <div class="voice"><div class="shot" role="img" aria-label="Black and white field of tall grass under an open sky" style="background:linear-gradient(180deg,#9a9a9a,#6a6a6a 55%,#3e3e3e)"></div>
      <div class="body"><b>Marcus, Veteran</b>"I fought for this country. Now I'm fighting for honest leadership."<span class="watch small"><i class="play"></i>Watch testimonial</span></div></div>
    <div class="voice"><div class="shot" role="img" aria-label="Black and white classroom with a teacher and students" style="background:linear-gradient(160deg,#e6e6e6,#a9a9a9 60%,#595959)"></div>
      <div class="body"><b>Linda, Teacher</b>"Our students deserve a democracy that tells the truth."<span class="watch small"><i class="play"></i>Watch</span></div></div>
    <div class="voice"><div class="shot" role="img" aria-label="Portrait placeholder for an entrepreneur" style="background:#2b2b2b"></div>
      <div class="body"><b>James, Entrepreneur</b>"Accountability shouldn't be partisan — it's common sense."<span class="watch"><i class="play"></i>Watch</span></div></div>
    <div class="voice"><div class="shot" role="img" aria-label="Black and white cyclist riding along a harbor with cranes" style="background:linear-gradient(180deg,#e0e0e0,#9c9c9c 60%,#6c6c6c)"></div>
      <div class="body"><b>Elena, Nurse</b>"Honest government means better care for all."<span class="watch"><i class="play"></i>Watch</span></div></div>
  </div>
</section>

<section class="final">
  <h2>History doesn't begin with politicians.<br>It begins with people.</h2>
  <p class="sub">This survey takes less than one minute.</p>
  <div class="vote-card">
    <h3>Cast your vote for honest governance</h3>
    <p>Should government be legally required to serve honestly?</p>
    <label><span class="radio"></span><span class="tick"></span>Yes — I demand honesty by law</label>
    <label class="no"><span class="radio"></span><span class="cross">✕</span>No, trust is enough</label>
    <div class="cast">CAST MY VOTE →</div>
  </div>
</section>

<footer>
  Lantern Square. Steady Course. — A nonpartisan civic movement. The next chapter begins with you.<br>
  © 2025 | Steady Course Civic Trust
</footer>

</body>
</html>
```